Web Design needed for logo design project

I am needing an interactive website for TC. Tandem Care Management is a nationwide company that combines the front desk administrative operation within Professional offices (Dental, Chiropractic, Optometry). I am needing a website designed that will provide information for potential new clients that are interested in joining our company to provide to them administrative support. I need a design for the marketing material within the folder, I will add content later. I am looking for clean crisp professional. No dancing teeth, hearts, or EKG signals please. We need it to appeal to 27-40 years old professionals. The professions are equally divided at 50/50 female to male. I already have a logo, it will be attached.
Updates

Target Market(s)

We need it to appeal to 27-40 years old professionals. The professions are equally divided at 50/50 female to male. I already have a logo, it will be attached.

Industry/Entity Type

Marketing

Requirements
Must have
• Needs to be in Word Press. It must have scalability to various screen sizes (Monitor, Phone screen, IPad, etc). Must have a customer portal capability, so professionals can access their information through a portal on the website. Have the capability to run a practice calculator or view a video requiring that it captures the visitors information so I can contact them regarding their interest in the site. Needs to have links to social media.

```html
<!DOCTYPE html>
<html lang="en">
<head>
<meta charset="utf-8">
<title>Tandem Care Management</title>
<link rel="stylesheet" href="https://fonts.googleapis.com/css2?family=Mulish:wght@300;400;500;600;700&display=swap">
<style>
:root{
  --navy:#123f73;
  --blue:#1c5b94;
  --sky:#3fa3d6;
  --ink:#222;
  --muted:#555;
  --rule:#e3e5e8;
  --footer-top:#215c95;
  --footer-bottom:#0f3769;
  --white:#fff;
}
*{box-sizing:border-box;margin:0;padding:0}
html,body{width:1108px;height:1200px;overflow:hidden;background:var(--white)}
body{font-family:"Mulish",sans-serif;color:var(--ink);position:relative}
.site-header{position:absolute;left:0;top:0;width:1108px;height:122px;background:var(--white)}
.brand{position:absolute;left:69px;top:38px;display:flex;align-items:center;gap:10px}
.brand-mark{width:34px;height:34px;background:var(--blue)}
.brand-name{font-size:25px;font-weight:700;color:var(--navy);letter-spacing:.5px}
.main-nav{position:absolute;left:535px;top:57px;display:flex;gap:33px}
.main-nav a{font-size:16px;font-weight:600;color:var(--navy);text-decoration:none}
.header-rule{position:absolute;left:0;top:122px;width:1108px;height:6px;background:var(--rule)}
.hero{position:absolute;left:0;top:128px;width:1108px;height:487px;overflow:hidden}
.hero-photo{position:absolute;inset:0;background:linear-gradient(90deg,#d7e0ea 0%,#eef2f6 30%,#f3f4f5 50%,#dfe6ee 72%,#c9d5e2 100%)}
.hero-copy{position:absolute;left:745px;top:125px}
.hero-title{font-size:35px;font-weight:300;color:var(--blue);letter-spacing:.5px}
.hero-sub{margin-top:8px;font-size:13px;line-height:16px;color:#444;width:230px}
.hero-actions{position:absolute;left:1px;top:93px;display:flex;gap:5px}
.btn{display:inline-block;font-family:inherit;font-weight:600;font-size:15px;color:var(--white);text-decoration:none;height:33px;line-height:33px;text-align:center}
.btn-portal{width:138px;background:var(--navy)}
.btn-login{width:92px;background:var(--sky)}
.slider-arrows{position:absolute;left:102px;top:427px}
.video-block{position:absolute;left:90px;top:637px;width:545px}
.section-title{font-size:36px;font-weight:300;color:var(--blue)}
.section-title small{font-size:14px;color:var(--muted);margin-left:6px}
.calc-link{position:absolute;left:423px;top:20px;font-size:13px;font-weight:500;color:var(--ink);text-decoration:none}
.video-frame{position:absolute;left:10px;top:54px;width:542px;height:263px;background:#d2d2d2;padding:5px}
.video-still{width:100%;height:100%;background:linear-gradient(135deg,#8f9aa6 0%,#b5b8b8 40%,#6b4b3e 70%,#c8c6c2 100%);position:relative}
.play{position:absolute;left:50%;top:50%;transform:translate(-50%,-50%)}
.welcome{position:absolute;left:678px;top:640px;width:340px}
.welcome p{margin-top:12px;font-size:11.2px;line-height:14.3px;color:var(--ink);text-align:justify}
.btn-more{display:inline-block;margin-top:25px;width:88px;height:32px;line-height:32px;text-align:center;background:var(--navy);color:var(--white);font-size:12px;text-decoration:none}
.site-footer{position:absolute;left:0;top:984px;width:1108px;height:216px;background:linear-gradient(180deg,var(--footer-top),var(--footer-bottom));color:var(--white)}
.footer-heading{font-size:16px;font-weight:500}
.quick-links{position:absolute;left:140px;top:34px}
.quick-links ul{list-style:none;display:grid;grid-template-columns:103px auto;row-gap:6px;margin-top:11px}
.quick-links a{color:var(--white);font-size:11.5px;text-decoration:none}
.contact{position:absolute;left:364px;top:34px}
.contact address{font-style:normal;font-size:11.5px;line-height:20.5px;margin-top:9px}
.map{position:absolute;left:494px;top:66px;width:165px;height:84px;background:linear-gradient(135deg,#e4e1d4,#d9d6c4 50%,#e8e3b9)}
.follow{position:absolute;left:715px;top:34px}
.social{display:flex;gap:8px;margin-top:16px}
.social span{width:26px;height:26px;border-radius:50%}
.s1{background:#3b5a96}.s2{background:#2aa3d9}.s3{background:#2d74a8}.s4{background:#c8324a}
.copyright{position:absolute;left:745px;top:180px;font-size:11.5px}
</style>
</head>
<body>
<header class="site-header">
  <div class="brand"><span class="brand-mark"></span><span class="brand-name">Tandem Care Management</span></div>
  <nav class="main-nav">
    <a href="#">Home</a><a href="#">About Us</a><a href="#">Services</a><a href="#">Blog</a><a href="#">Contact Us</a>
  </nav>
</header>
<div class="header-rule"></div>

<section class="hero">
  <div class="hero-photo" role="img" aria-label="Smiling professional in shirt and tie seated at a laptop in a bright office"></div>
  <div class="hero-copy">
    <h1 class="hero-title">Lorium Ipsum</h1>
    <p class="hero-sub">Many desktop publishing packages and web page editors now use</p>
    <div class="hero-actions">
      <a class="btn btn-portal" href="#">Customer Portal</a>
      <a class="btn btn-login" href="#">Login</a>
    </div>
  </div>
  <svg class="slider-arrows" width="47" height="33" viewBox="0 0 47 33" aria-label="Slide controls">
    <polygon points="20,0 20,33 0,16.5" fill="#1c5b94"/>
    <polygon points="27,0 27,33 47,16.5" fill="#1c5b94"/>
  </svg>
</section>

<section class="video-block">
  <h2 class="section-title">Video<small>See our Video</small></h2>
  <a class="calc-link" href="#">Practise Calculator</a>
  <div class="video-frame">
    <div class="video-still" role="img" aria-label="Overhead view of a team meeting around a table with charts and a laptop">
      <svg class="play" width="54" height="54" viewBox="0 0 54 54" aria-label="Play video">
        <circle cx="27" cy="27" r="27" fill="#222" opacity=".85"/>
        <polygon points="22,16 22,38 38,27" fill="#fff"/>
      </svg>
    </div>
  </div>
</section>

<section class="welcome">
  <h2 class="section-title">Welcome</h2>
  <p>Duis aute irure dolor in reprehenderit in voluptate velit esse cillum dolore eu fugiat nulla pariatur. Excepteur sint occaecat cupidatat non proident, sunt in culpa qui officia deserunt mollit anim id est laborum Nemo enim ipsam voluptatem quia voluptas sit aspernatur aut odit aut fugit, sed quia consequuntur magni dolores eos qui ratione voluptatem sequi nesciunt. Neque porro quisquam est, qui dolorem ipsum quia dolor sit amet, consectetur, adipisci velit, sed quia non numquam eius modi tempora incidunt ut labore et dolore magnam aliquam quaerat voluptatem. Ut enim ad minima veniam, quis nostrum exercitationem ullam Nemo enim ipsam voluptatem quia voluptas sit aspernatur aut odit aut fugit, sed quia consequuntur magni dolores eos Nemo enim ipsam voluptatem quia voluptas sit aspernatur aut odit aut fugit,</p>
  <a class="btn-more" href="#">Read more</a>
</section>

<footer class="site-footer">
  <div class="quick-links">
    <h3 class="footer-heading">Quick Links</h3>
    <ul>
      <li><a href="#">Home</a></li><li><a href="#">Blog</a></li>
      <li><a href="#">About Us</a></li><li><a href="#">Contact Us</a></li>
      <li><a href="#">Services</a></li>
    </ul>
  </div>
  <div class="contact">
    <h3 class="footer-heading">Contact</h3>
    <address>X12 , Lorium ipsum<br>Phone: +13 6 555 0142<br>57 Harbour Lane<br>New Zealand</address>
  </div>
  <div class="map" role="img" aria-label="Street map showing the office location"></div>
  <div class="follow">
    <h3 class="footer-heading">Follow Us</h3>
    <div class="social"><span class="s1"></span><span class="s2"></span><span class="s3"></span><span class="s4"></span></div>
  </div>
  <p class="copyright">©2014.www.tandemcaremgmt.com</p>
</footer>
</body>
</html>
```